Business Card Design

We need a business card design for a new dental practice in Brisbane. I'd like the basic details and logo on one side and appointment schedule on the other side. It is based in CBD office area and would prefer a professional and modern design.
Target Market(s)
20-60 years old office workers and residents with high education levels
Industry/Entity Type
Dental
Contact Information for Business Card
Harbourlight Dental
Dr Glenn Marwick
Principal Dentist
07 3964 2275
admin@harbourlightsmiles.com.au
www.harbourlightsmiles.com.au
S27, Level 3, Ardent North Plaza, 814 Tallowood Rd, Kelsey Heights, QLD 4019

```html
<!DOCTYPE html>
<html lang="en">
<head>
<meta charset="utf-8">
<title>Harbourlight Dental – Business Card</title>
<link rel="stylesheet" href="https://fonts.googleapis.com/css2?family=Quicksand:wght@500;600;700&display=swap">
<style>
  :root {
    --backdrop: #232426;
    --card: #ffffff;
    --navy: #0d1e2b;
    --sky: #4fb1e3;
    --sky-light: #7fc6ee;
    --ink: #14222e;
  }
  * { box-sizing: border-box; margin: 0; padding: 0; }
  html, body {
    width: 1200px; height: 900px; overflow: hidden;
    background: var(--backdrop);
    font-family: "Quicksand", sans-serif;
  }
  .stage {
    position: relative; width: 1200px; height: 900px;
    display: flex; justify-content: center; align-items: center; gap: 60px;
  }
  .card {
    position: relative; width: 400px; height: 620px;
    background: var(--card); border-radius: 14px; overflow: hidden;
    box-shadow: 0 14px 30px rgba(0,0,0,.45);
  }
  .card__wave { position: absolute; left: 0; bottom: 0; width: 400px; height: 170px; display: block; }

  .brand { display: flex; align-items: center; justify-content: center; gap: 12px; }
  .brand__dot { width: 34px; height: 34px; border-radius: 50%; background: var(--sky); flex: none; }
  .brand__name { font-weight: 600; color: var(--ink); }

  .card--front .brand { margin-top: 120px; }
  .card--front .brand__name { font-size: 36px; letter-spacing: .3px; }

  .person { margin-top: 70px; padding-right: 40px; text-align: right; }
  .person__name { font-size: 30px; font-weight: 600; color: var(--sky); }
  .person__role { font-size: 19px; font-weight: 600; color: var(--ink); margin-top: 4px; }

  .contact { margin-top: 70px; padding-right: 34px; text-align: right; font-size: 16px; font-weight: 600; color: var(--ink); line-height: 1.5; }
  .contact__label { color: var(--sky); }

  .card--back .brand { margin-top: 90px; }
  .card--back .brand__name { font-size: 24px; }
  .appointment__title { margin-top: 22px; text-align: center; font-size: 26px; font-weight: 700; color: var(--ink); letter-spacing: 1px; }
  .appointment__fields { list-style: none; margin-top: 36px; padding-left: 32px; }
  .appointment__fields li { font-size: 17px; font-weight: 600; color: var(--sky); margin-bottom: 14px; }
</style>
</head>
<body>
<main class="stage">

  <article class="card card--front">
    <div class="brand">
      <span class="brand__dot"></span>
      <span class="brand__name">Harbourlight Dental</span>
    </div>
    <div class="person">
      <p class="person__name">Dr. Glenn Marwick</p>
      <p class="person__role">Principal Dentist</p>
    </div>
    <div class="contact">
      <p><span class="contact__label">T:</span> 07 3964 2275</p>
      <p><span class="contact__label">A:</span> S27, Level 3, Ardent North Plaza</p>
      <p>814 Tallowood Rd, Kelsey Heights, QLD 4019</p>
    </div>
    <svg class="card__wave" viewBox="0 0 400 170" preserveAspectRatio="none" aria-hidden="true">
      <path d="M0 0 C120 40 260 50 400 30 L400 170 L0 170 Z" fill="var(--sky)"/>
      <path d="M0 40 C130 70 270 60 400 40 L400 170 L0 170 Z" fill="#ffffff"/>
      <path d="M0 56 C130 86 270 74 400 56 L400 170 L0 170 Z" fill="var(--navy)"/>
    </svg>
  </article>

  <article class="card card--back">
    <div class="brand">
      <span class="brand__dot"></span>
      <span class="brand__name">Harbourlight Dental</span>
    </div>
    <h1 class="appointment__title">APPOINTMENT</h1>
    <ul class="appointment__fields">
      <li>Date:</li>
      <li>Time:</li>
      <li>Reason for Visit:</li>
    </ul>
    <svg class="card__wave" viewBox="0 0 400 170" preserveAspectRatio="none" aria-hidden="true">
      <path d="M0 0 C40 80 170 120 400 110 L400 170 L0 170 Z" fill="var(--navy)"/>
      <path d="M0 10 C50 80 180 120 400 118 L400 170 L0 170 Z" fill="#ffffff"/>
      <path d="M0 22 C60 90 190 126 400 128 L400 170 L0 170 Z" fill="var(--sky)"/>
      <path d="M150 120 C250 110 330 95 400 70 L400 150 C320 140 230 132 150 120 Z" fill="var(--sky-light)"/>
      <path d="M0 60 C80 130 220 150 400 150 L400 170 L0 170 Z" fill="#ffffff"/>
      <path d="M0 72 C90 140 230 158 400 158 L400 170 L0 170 Z" fill="var(--navy)"/>
    </svg>
  </article>

</main>
</body>
</html>
```